Harborline Stay Collective Business Card Design

Design a business card for Harborline Stay Collective. Look at the website for colors and reference. Card should have logo, name, title, office number, mobile number, email, URL and a tagline like, "Luxury Hotel & Resort Email Marketing" (This might change).

https://www.harborlinestaycollective.net

The rest I will leave up to your imagination.

Contact Information for Business Card

Logo, name, title, office number, mobile number, email, URL and a tagline like, "Luxury Hotel & Resort Email Marketing" (This might change).

```html
<!DOCTYPE html>
<html lang="en">
<head>
<meta charset="utf-8">
<title>Harborline Stay Collective – Business Card</title>
<link rel="stylesheet" href="https://fonts.googleapis.com/css2?family=Lato:wght@400;700;900&family=Dancing+Script:wght@600&display=swap">
<style>
  :root {
    --bg: #4a4a4a;
    --card: #1c1c1c;
    --orange: #f47a00;
    --silver-light: #e4e4e4;
    --silver-dark: #8c8c8c;
    --ink: #1c1c1c;
    --text: #f2f2f2;
  }
  * { box-sizing: border-box; margin: 0; padding: 0; }
  html, body { width: 1200px; height: 689px; overflow: hidden; }
  body {
    background: var(--bg);
    font-family: "Lato", sans-serif;
    display: flex; align-items: center; justify-content: center; gap: 48px;
  }
  .card {
    position: relative;
    width: 540px; height: 310px;
    background: var(--card);
    box-shadow: 0 18px 40px rgba(0,0,0,.45);
    overflow: hidden;
    color: var(--text);
  }
  /* front */
  .corner-chip {
    position: absolute; right: 0; top: 0; width: 44px; height: 30px;
    background: linear-gradient(135deg, var(--silver-dark), var(--silver-light));
  }
  .name-band {
    position: absolute; left: 0; top: 108px;
    width: 290px; height: 40px;
    background: var(--orange);
    clip-path: polygon(0 0, 100% 0, 94% 100%, 0 100%);
    padding-left: 30px;
    display: flex; align-items: center;
  }
  .person-name {
    font-weight: 900; font-size: 23px; letter-spacing: 1px; color: var(--ink);
    white-space: nowrap;
  }
  .title-band {
    position: absolute; left: 0; top: 148px;
    width: 160px; height: 26px;
    background: linear-gradient(90deg, var(--silver-dark), var(--silver-light));
    clip-path: polygon(0 0, 100% 0, 90% 100%, 0 100%);
    padding-left: 34px;
    display: flex; align-items: center;
  }
  .person-title { font-size: 13px; color: var(--ink); white-space: nowrap; }
  .brand-mark {
    position: absolute; display: flex; align-items: center; gap: 10px;
    font-weight: 900; color: var(--text);
    letter-spacing: 1px; text-transform: uppercase; white-space: nowrap;
  }
  .brand-mark .dot { background: var(--orange); flex: none; }
  .card-front .brand-mark { right: 40px; top: 62px; font-size: 15px; }
  .card-front .brand-mark .dot { width: 12px; height: 12px; }
  .address {
    position: absolute; right: 40px; top: 150px; text-align: right;
    font-size: 13px; line-height: 1.45; font-style: normal;
  }
  .address .company { color: var(--orange); }
  .contacts {
    position: absolute; left: 36px; bottom: 30px;
    list-style: none; font-size: 13px; line-height: 1.55;
  }
  .contacts li { display: flex; align-items: center; gap: 10px; white-space: nowrap; }
  .contacts svg { width: 11px; height: 11px; fill: var(--orange); flex: none; }
  /* back */
  .card-back .brand-mark {
    left: 50%; top: 118px; transform: translateX(-50%);
    font-size: 26px;
  }
  .card-back .brand-mark .dot { width: 20px; height: 20px; }
  .tagline {
    position: absolute; left: 0; right: 0; top: 200px; text-align: center;
    font-family: "Dancing Script", cursive; font-size: 22px; color: var(--text);
  }
</style>
</head>
<body>
  <section class="card card-front">
    <div class="corner-chip"></div>
    <div class="brand-mark"><span class="dot"></span>Harborline Stay Collective</div>
    <div class="name-band"><span class="person-name">DANIEL REYES</span></div>
    <div class="title-band"><span class="person-title">Founder &amp; CEO</span></div>
    <address class="address">
      <div class="company">Harborline Stay Collective</div>
      <div>4710 Cedar Point Road, Ste 8</div>
      <div>Milford, CT 06460</div>
    </address>
    <ul class="contacts">
      <li><svg viewBox="0 0 12 12"><path d="M2.5 0.5l2 2.2-1 1.3c.7 1.6 1.9 2.8 3.5 3.5l1.3-1 2.2 2-1.2 2.5C4.6 10.7 1.3 7.4.2 1.7z"/></svg>(203) 555-0147</li>
      <li><svg viewBox="0 0 12 12"><path d="M3 0h6a1 1 0 0 1 1 1v10a1 1 0 0 1-1 1H3a1 1 0 0 1-1-1V1a1 1 0 0 1 1-1zm.5 1.5v7.5h5V1.5z"/></svg>(203) 555-0182</li>
      <li><svg viewBox="0 0 12 12"><path d="M0 2h12v8H0zm1 1v.4l5 3.3 5-3.3V3z"/></svg>info@harborlinestaycollective.net</li>
      <li><svg viewBox="0 0 12 12"><circle cx="6" cy="6" r="5.5"/></svg>harborlinestaycollective.net</li>
    </ul>
  </section>

  <section class="card card-back">
    <div class="brand-mark"><span class="dot"></span>Harborline Stay Collective</div>
    <p class="tagline">Luxury Hotel &amp; Resort Email Marketing</p>
  </section>
</body>
</html>
```